Organic Ready Meal/Food Packaging Design

We are looking to re-vamp/re-design our current food packaging. The design will be for an outer box surround for our food which is packed into plastic pots. The meals are fresh and ready to eat. There are 4 variants (recipes) and one design is needed with a background colour change for each recipe. I am looking for a fresh, modern and eye-catching look which stands out on a supermarket shelf. It should be noted that there there is an existing design which needs an overhaul. I would like the winning bidder to look at this together with some other types of packaging I like to improve it.

I have attached a copy of my existing packaging which can also be seen on our company website www.thebraxfoods.com. We need to move away from this bitty, wishy washy theme to something brighter and bolder, more modern and innovative like the 'Tub o' example I have also attached. Other points of reference are www.dornakitchen.co.uk and www.figlettots.co.uk which are bright and eye-catching. The Dorna Bakes 'tub o' boxes are a good benchmark for us although we do not want to copy the design.

This project probably needs to incorporate a modified company logo and the budget can be modified to include this.

We also need to use the word 'Tasty' as a sub-header for our meals i.e.

Tasty
Organic Mediterranean Bean Casserole

Any other questions, please ask at any time.

Target Market(s)

anybody wanting a healthy, organic ready meal
men
women
mums

Industry/Entity Type

It Company

Requirements
Must have
• Bold modern colours/design
Modern eye catching design/fonts
Should not have
• Illustrations (sketchy drawings)

```html
<!DOCTYPE html>
<html lang="en">
<head>
<meta charset="utf-8">
<title>Brax Foods – Tasty Red Lentil &amp; Vegetable Soup Sleeve</title>
<link rel="stylesheet" href="https://fonts.googleapis.com/css2?family=Montserrat:wght@500;600;800&display=swap">
<style>
  :root {
    --page: #ffffff;
    --kraft: #c9a878;
    --kraft-edge: #b8966a;
    --plum: #3e1e2e;
    --plum-pattern: #4b2839;
    --magenta: #d2409c;
    --white: #ffffff;
  }
  * { margin: 0; padding: 0; box-sizing: border-box; }
  html, body {
    width: 1200px; height: 1071px; overflow: hidden;
    background: var(--page);
  }
  .sleeve {
    position: absolute; left: 255px; top: 208px;
    width: 694px; height: 664px;
    background: var(--kraft);
    border: 1px solid var(--kraft-edge);
  }
  .sleeve__panel {
    position: absolute; left: 13px; top: 13px; right: 13px; bottom: 13px;
    background: var(--plum);
    overflow: hidden;
  }
  .sleeve__pattern {
    position: absolute; left: 0; right: 0; bottom: 0; height: 300px;
    background: linear-gradient(180deg, rgba(75,40,57,0) 0%, var(--plum-pattern) 30%, var(--plum-pattern) 100%);
  }
  .brand {
    position: absolute; left: 0; right: 0; top: 136px;
    text-align: center;
    font-family: "Montserrat", sans-serif; font-weight: 600;
    font-size: 28px; color: var(--white);
  }
  .range-title {
    position: absolute; left: 30px; top: 222px;
    font-family: "Montserrat", sans-serif; font-weight: 800;
    font-size: 150px; line-height: 1; color: var(--magenta);
    letter-spacing: 4px;
  }
  .fresh-badge {
    position: absolute; left: 510px; top: 342px;
    width: 128px; height: 86px;
  }
  .fresh-badge svg { position: absolute; left: 0; top: 0; }
  .fresh-badge__text {
    position: absolute; left: 0; right: 0; top: 20px;
    text-align: center;
    font-family: "Montserrat", sans-serif; font-weight: 800;
    font-size: 20px; line-height: 23px; color: var(--white);
  }
  .product-claim {
    position: absolute; left: 78px; top: 370px;
    font-family: "Montserrat", sans-serif; font-weight: 800;
    font-size: 38px; line-height: 1; color: var(--white);
  }
  .product-name {
    position: absolute; left: 84px; top: 418px;
    font-family: "Montserrat", sans-serif; font-weight: 800;
    font-size: 38px; line-height: 52px; color: var(--magenta);
    text-transform: uppercase;
  }
  .servings {
    position: absolute; right: 18px; bottom: 18px;
    font-family: "Montserrat", sans-serif; font-weight: 500;
    font-size: 15px; color: var(--white);
  }
</style>
</head>
<body>
  <main class="sleeve">
    <div class="sleeve__panel">
      <div class="sleeve__pattern" role="img" aria-label="Faint tonal floral pattern across the lower half of the sleeve"></div>

      <p class="brand">The Brax Foods</p>

      <h1 class="range-title">TASTY</h1>

      <div class="fresh-badge">
        <svg width="128" height="86" viewBox="0 0 128 86" aria-hidden="true">
          <path d="M24 8 Q64 -2 108 8 Q126 14 124 42 Q122 72 96 78 Q64 86 30 78 Q6 72 6 44 Q4 28 12 18 Q2 6 -2 2 Q14 8 24 8 Z" fill="var(--magenta)"/>
        </svg>
        <p class="fresh-badge__text">FRESH<br>FOOD</p>
      </div>

      <p class="product-claim">100% ORGANIC</p>
      <h2 class="product-name">Red Lentil &amp;<br>Vegetable Soup</h2>

      <p class="servings">SERVINGS 1-2</p>
    </div>
  </main>
</body>
</html>
```